DOUBLE SIDED BROCHURE NEEDED TO PROMOTE DOCTOR

I need a double sided DL size (99mm x 210mm) brochure, promoting a doctor seeing patients in a new area.

I want something professional. I have included the relevant information. I would also like the Dr's picture somwhere in the brochure, with a professional background. I wish to print these tomorrow, so i will pick a winner within 14 hours of posting this ad.

I have included an example of a brochures design that I recently saw, and its definietly a good starting point.

Medical

```html
<!DOCTYPE html>
<html lang="en">
<head>
<meta charset="utf-8">
<title>Dr. Haddad – DL Brochure</title>
<link href="https://fonts.googleapis.com/css2?family=Teko:wght@500;600&family=Titillium+Web:wght@300;400;600;700&display=swap" rel="stylesheet">
<style>
:root{
  --navy:#0a3a8c;
  --royal:#0b4ea2;
  --sky-light:#cdeaf4;
  --sky-mid:#a6d9ea;
  --sky-deep:#62bcd8;
  --ink:#1f3a4d;
  --red:#e31b23;
  --grey-band:#d2d5d8;
  --white:#ffffff;
  --stage:#e9ecef;
}
*{margin:0;padding:0;box-sizing:border-box}
html,body{width:1200px;height:1053px;overflow:hidden;background:var(--stage)}
body{position:relative;font-family:"Titillium Web",Arial,sans-serif;color:var(--ink)}
.panel{position:absolute;top:50px;width:459px;height:953px;overflow:hidden;
  background:linear-gradient(160deg,var(--sky-light) 0%,var(--sky-mid) 55%,var(--sky-deep) 100%)}
.panel--front{left:96px}
.panel--back{left:624px}
.panel svg.shapes{position:absolute;left:0;top:0}
.headline{font-family:"Teko",Impact,sans-serif;font-weight:600;color:var(--navy);line-height:.86;letter-spacing:.5px}
.doctor-name{position:absolute;left:32px;top:346px;font-size:50px}
.intro{position:absolute;left:32px;top:394px;font-size:19.5px;line-height:30px;font-weight:400;white-space:nowrap}
.services{position:absolute;left:32px;list-style:none;font-size:19.5px;white-space:nowrap}
.services li{position:relative;padding-left:24px;height:33px;line-height:33px}
.services li::before,.services li::after{content:"";position:absolute;background:var(--red)}
.services li::before{left:4px;top:10px;width:6px;height:14px}
.services li::after{left:0;top:14px;width:14px;height:6px}
.services .note{display:block;font-size:15.5px;line-height:18px;margin-top:-6px}
.services--specialty li{height:34px}
.services--specialty li.with-note{height:57px}
.services--specialty{top:487px}
.subhead{position:absolute;left:32px;top:654px;font-size:19.5px;font-weight:600;color:var(--navy);white-space:nowrap}
.services--general{top:688px}
.footer-strip{position:absolute;left:0;width:100%}
.front-footer{top:868px;height:85px;background:var(--royal);border-top:13px solid var(--white);display:flex;align-items:center;padding-left:32px;gap:10px}
.footer-phone{color:var(--white);font-size:25px;font-weight:700}
.icon-phone{width:26px;height:26px}
.dear{position:absolute;left:36px;top:166px;font-size:64px}
.letter{position:absolute;left:40px;font-size:20.5px;line-height:33px;font-weight:300;color:#2d4250;white-space:nowrap}
.letter--one{top:293px}
.letter--two{top:458px}
.clinic-box{top:667px;height:195px;background:var(--white);border-top:13px solid var(--grey-band);border-bottom:13px solid var(--grey-band)}
.clinic-name{position:absolute;left:30px;top:20px;font-size:36px}
.clinic-line{position:absolute;left:58px;font-size:18px;line-height:21px;color:#2d3a44}
.clinic-address{top:68px}
.clinic-phone{top:125px;font-weight:700;font-size:21px}
.clinic-icon{position:absolute;left:34px}
.big-cross{position:absolute;left:295px;top:608px;width:129px;height:129px}
.referral{top:862px;height:91px;background:var(--royal);color:var(--white);text-align:center;padding-top:20px}
.referral p{font-size:18px;line-height:22px}
.referral strong{display:block;font-size:28px;line-height:32px;font-weight:700}
</style>
</head>
<body>

<section class="panel panel--front">
  <svg class="shapes" width="459" height="953" viewBox="0 0 459 953">
    <defs>
      <linearGradient id="photoTone" x1="0" y1="0" x2="1" y2="1">
        <stop offset="0" stop-color="#8fb4d6"/>
        <stop offset=".55" stop-color="#b9c9d6"/>
        <stop offset="1" stop-color="#6d6a6c"/>
      </linearGradient>
    </defs>
    <polygon points="0,0 459,0 459,48" fill="var(--royal)"/>
    <polygon points="0,0 459,48 459,345 0,281" fill="url(#photoTone)" role="img" aria-label="Portrait of Dr. Haddad in front of Riverside General Hospital"/>
    <polygon points="0,281 459,345 459,364 0,292" fill="var(--royal)"/>
    <polygon points="0,292 459,364 459,390 0,306" fill="#ffffff" opacity=".35"/>
  </svg>

  <h1 class="headline doctor-name">DR. HADDAD</h1>
  <p class="intro">is a highly trained specialised<br>surgeon, in all areas of Endocrine,<br>Breast and General Surgery. Including;</p>

  <ul class="services services--specialty">
    <li>Thyroid Surgery</li>
    <li class="with-note">Parathyroid surgery<span class="note">(including minimally invasive parathyroidectomy)</span></li>
    <li>Breast Cancer</li>
    <li>Benign breast lesions</li>
  </ul>

  <h2 class="subhead">All areas of general surgery, such as;</h2>
  <ul class="services services--general">
    <li>Gallbladder surgery</li>
    <li>Hernia surgery</li>
    <li>Haemorrhoids</li>
    <li>Carpal Tunnel</li>
    <li>Vasectomy etc etc...</li>
  </ul>

  <div class="footer-strip front-footer">
    <svg class="icon-phone" viewBox="0 0 24 24" fill="none" stroke="#fff" stroke-width="1.6" stroke-linejoin="round">
      <path d="M5 3h4l2 5-2.5 1.5a11 11 0 0 0 6 6L16 13l5 2v4a2 2 0 0 1-2 2A16 16 0 0 1 3 5a2 2 0 0 1 2-2z"/>
      <path d="M15 3a6 6 0 0 1 6 6M15 6.5a2.5 2.5 0 0 1 2.5 2.5"/>
    </svg>
    <span class="footer-phone">1300 482 716</span>
  </div>
</section>

<section class="panel panel--back">
  <svg class="shapes" width="459" height="953" viewBox="0 0 459 953">
    <polygon points="0,0 459,0 459,153 0,90" fill="var(--royal)"/>
    <polygon points="0,90 459,153 459,191 0,110" fill="#ffffff" opacity=".45"/>
    <rect x="137" y="26" width="304" height="116" rx="10" fill="#2a66b3" role="img" aria-label="Illustration of a calendar, heart monitor and two medical staff"/>
  </svg>

  <h1 class="headline dear">DEAR<br>DOCTORS,</h1>
  <p class="letter letter--one">We are pleased to announce that<br>Dr. Karim Haddad is now consulting in<br>Bayside, seeing public and<br>private patients.</p>
  <p class="letter letter--two">Guaranteed appointment within<br>two weeks, with patients having<br>the option of surgery at Coastal Health<br>Campus, Riverside General Hospital or<br>St. Clare Westfield.</p>

  <div class="footer-strip clinic-box">
    <h2 class="headline clinic-name">BAYSIDE CLINIC</h2>
    <svg class="clinic-icon" style="top:69px" width="14" height="20" viewBox="0 0 14 20">
      <path d="M7 0a7 7 0 0 1 7 7c0 5-7 13-7 13S0 12 0 7a7 7 0 0 1 7-7z" fill="var(--royal)"/>
      <circle cx="7" cy="7" r="2.6" fill="#fff"/>
    </svg>
    <p class="clinic-line clinic-address">42 Harbour View Road<br>Bayside WA 6999</p>
    <svg class="clinic-icon" style="top:127px" width="20" height="20" viewBox="0 0 24 24" fill="none" stroke="var(--royal)" stroke-width="1.8" stroke-linejoin="round">
      <path d="M5 3h4l2 5-2.5 1.5a11 11 0 0 0 6 6L16 13l5 2v4a2 2 0 0 1-2 2A16 16 0 0 1 3 5a2 2 0 0 1 2-2z"/>
    </svg>
    <p class="clinic-line clinic-phone">1300 482 716</p>
  </div>

  <svg class="big-cross" viewBox="0 0 129 129">
    <rect x="40" y="0" width="49" height="129" fill="var(--red)"/>
    <rect x="0" y="40" width="129" height="49" fill="var(--red)"/>
  </svg>

  <div class="footer-strip referral">
    <p>Please send all referrals by fax to<strong>(08) 6204 5831</strong></p>
  </div>
</section>

</body>
</html>
```